For Lease sign for Property management company in Kansas City

We need someone to take our information and design a standard for lease sign that we can put in front of each of our buildings. I would love for it to do its job of letting people know there are units available but also be unique somehow. Also the aspect ratio of the design would ideally be 4 wide by 3 tall but we open to other ideas. It will be a larger yard sign.

Target Market(s)

Potential Tenants

Industry/Entity Type

Real Estate Development

Font styles to use
Sans Serif

Requirements
Must have
• Our logo, our website (www.quillstead-properties.com), our phone number (816) 555-2719.
Nice to have
• Some how say "For Lease"
Sign to be 4' wide by 3' tall
If there was a place to put the building name that would be cool but not ne
Should not have
• Nothing that I can think of

```html
<!DOCTYPE html>
<html lang="en">
<head>
<meta charset="utf-8">
<title>Quillstead Properties – For Lease Sign</title>
<link href="https://fonts.googleapis.com/css2?family=Anton&family=Montserrat:wght@700&family=Oswald:wght@700&display=swap" rel="stylesheet">
<style>
  :root {
    --page-bg: #e4e4e4;
    --sign-white: #ffffff;
    --sign-grey: #dcdcdc;
    --brand-red: #be1e2d;
    --deep-red: #861c2a;
    --amber: #fbb040;
    --amber-edge: #d9963a;
    --ink-grey: #58595b;
  }
  html, body {
    margin: 0;
    padding: 0;
    width: 1200px;
    height: 1200px;
    overflow: hidden;
    background: var(--page-bg);
  }
  .lease-sign {
    position: absolute;
    left: 0;
    top: 150px;
    width: 1200px;
    height: 900px;
    display: block;
  }
  .brand-name { font-family: 'Montserrat', sans-serif; font-weight: 700; fill: var(--brand-red); }
  .lease-label { font-family: 'Anton', sans-serif; fill: var(--amber); }
  .phone-number { font-family: 'Montserrat', sans-serif; font-weight: 700; fill: var(--deep-red); }
  .website { font-family: 'Oswald', sans-serif; font-weight: 700; fill: var(--ink-grey); }
  .phone-icon { fill: var(--deep-red); }
</style>
</head>
<body>
<svg class="lease-sign" viewBox="0 0 1200 900" xmlns="http://www.w3.org/2000/svg" aria-label="For lease sign by Quillstead Properties">
  <defs>
    <linearGradient id="panelShade" x1="0" y1="0" x2="1" y2="0">
      <stop offset="0" stop-color="var(--sign-grey)"/>
      <stop offset="0.45" stop-color="var(--sign-white)"/>
      <stop offset="1" stop-color="var(--sign-white)"/>
    </linearGradient>
  </defs>

  <rect class="sign-panel" x="0" y="0" width="1200" height="900" fill="url(#panelShade)"/>

  <g class="brand-header">
    <circle class="brand-dot" cx="221" cy="179" r="150" fill="var(--amber)" stroke="var(--amber-edge)" stroke-width="5"/>
    <text class="brand-name" x="432" y="205" font-size="116" textLength="700" lengthAdjust="spacingAndGlyphs">QUILLSTEAD</text>
    <text class="brand-name" x="432" y="323" font-size="100" textLength="700" lengthAdjust="spacingAndGlyphs">PROPERTIES</text>
  </g>

  <g class="lease-band">
    <rect x="0" y="354" width="1200" height="295" fill="var(--amber)"/>
    <polygon class="lease-arrow" points="0,354 519,354 599,501 519,649 0,649" fill="var(--deep-red)"/>
    <text class="lease-label" x="188" y="463" font-size="107" textLength="191" lengthAdjust="spacingAndGlyphs">FOR</text>
    <text class="lease-label" x="66" y="627" font-size="165" textLength="436" lengthAdjust="spacingAndGlyphs">LEASE</text>
  </g>

  <g class="contact">
    <svg class="phone-icon" x="44" y="672" width="110" height="110" viewBox="0 0 24 24">
      <path d="M6.62 10.79c1.44 2.83 3.76 5.14 6.59 6.59l2.2-2.2c.27-.27.67-.36 1.020-.24 1.12.37 2.33.57 3.57.57.55 0 1 .45 1 1V20c0 .55-.45 1-1 1-9.39 0-17-7.610-17-17 0-.55.45-1 1-1h3.5c.55 0 1 .45 1 1 0 1.25.2 2.45.57 3.57.11.35.03.74-.25 1.02l-2.2 2.2z"/>
      <path d="M19 12h2a9 9 0 0 0-9-9v2c3.87 0 7 3.13 7 7zm-4 0h2c0-2.76-2.24-5-5-5v2c1.66 0 3 1.34 3 3z"/>
    </svg>
    <text class="phone-number" x="182" y="768" font-size="130" textLength="962" lengthAdjust="spacingAndGlyphs">(816) 555-2719</text>
    <text class="website" x="95" y="866" font-size="62" textLength="1010" lengthAdjust="spacingAndGlyphs">www.quillstead-properties.com</text>
  </g>
</svg>
</body>
</html>
```